Flier redesign 2021

The 3 prior year fliers are attached. We want a new design for 2021 -

* DO NOT SIMPLY COPY and change the year.
*All text should be the same, except year is 2021.
*Use different photos. You can find photos on our website maplecrestgardens.org or on our google page.

Requirements
Must have
• MUST be done in photoshop an photoshop file must be provided at the end.
Should not have
• Should not be same design as previous years.

```html
<!DOCTYPE html>
<html lang="en">
<head>
<meta charset="utf-8">
<title>Maplecrest Gardens – 2021 Landscaping Packages</title>
<link href="https://fonts.googleapis.com/css2?family=Big+Shoulders+Inline+Display:wght@600&family=Roboto:wght@400;500;700&family=Roboto+Condensed:wght@700&display=swap" rel="stylesheet">
<style>
  :root{
    --backdrop:#5e1419;
    --crimson:#8b1a1e;
    --brick:#c43d27;
    --wine:#a0202a;
    --panel-grey:#f3f4f6;
    --peach:#fdd9b5;
    --ribbon:#f0a64a;
    --ink:#2b2b2b;
    --white:#ffffff;
  }
  *{margin:0;padding:0;box-sizing:border-box}
  html,body{width:1200px;height:1200px;overflow:hidden}
  body{background:var(--backdrop);font-family:"Roboto",Arial,sans-serif;color:var(--ink)}
  .canvas{position:relative;width:1200px;height:1200px;overflow:hidden}
  .flier-base{position:absolute;left:184px;top:60px;width:832px;height:1077px;background:var(--crimson)}
  .hero-photo{position:absolute;left:184px;top:60px;width:832px;height:418px;
    background:linear-gradient(90deg,#5f7a2c 0%,#7d8a3a 18%,#b8456e 34%,#a1254a 48%,#d9823a 62%,#e89a2a 80%,#d07a1c 100%)}
  .shapes{position:absolute;left:0;top:0}
  .brand-tab{position:absolute;left:520px;top:60px;width:160px;height:152px;background:var(--white);
    border-radius:0 0 8px 8px;display:flex;flex-direction:column;align-items:center;justify-content:center;gap:4px}
  .brand-mark{width:14px;height:14px;border-radius:50%;background:var(--crimson);margin-bottom:6px}
  .brand-name{font-family:"Roboto",Arial,sans-serif;font-weight:500;color:var(--crimson);font-size:21px;line-height:1.15;text-align:center;letter-spacing:.5px}
  .title{position:absolute;left:223px;top:413px;width:754px;height:136px;display:flex;align-items:center;justify-content:center;
    font-family:"Big Shoulders Inline Display",Impact,sans-serif;font-weight:600;font-size:84px;line-height:1;color:var(--white);
    white-space:nowrap;padding-top:6px}
  .title-text{display:inline-block;transform:scaleX(0.8);transform-origin:center}
  .col-head{position:absolute;top:562px;color:var(--white);font-family:"Roboto Condensed",Arial Narrow,sans-serif;font-weight:700;
    font-size:21px;line-height:25px;text-align:center;display:flex;align-items:center;justify-content:center}
  .ribbon{position:absolute;left:443px;top:591px;width:110px;height:18px;background:var(--ribbon);color:var(--crimson);
    font-family:"Roboto Condensed",Arial Narrow,sans-serif;font-weight:700;font-size:9.5px;line-height:18px;text-align:center;transform:rotate(-45deg)}
  .col{position:absolute;top:680px;text-align:center}
  .col-sub{font-weight:500;font-size:16.5px;line-height:20px;color:var(--wine)}
  .features{list-style:none;text-align:left;margin-top:20px}
  .features li{position:relative;padding-left:20px;font-size:12.3px;line-height:16px;margin-bottom:14px}
  .features li::before{content:"";position:absolute;left:3px;top:2px;width:5px;height:9px;border-right:2.2px solid var(--wine);border-bottom:2.2px solid var(--wine);transform:rotate(40deg)}
  .price-block{position:absolute;left:0;width:100%;text-align:center}
  .term{font-size:10.5px;letter-spacing:.4px;color:#444}
  .amount{font-weight:700;font-size:30px;line-height:34px;color:var(--crimson)}
  .amount sup{font-size:13px;font-weight:500;vertical-align:13px;margin-right:3px}
  .fine{position:absolute;left:0;width:100%;text-align:center;font-size:12px;line-height:18px;color:#333}
  .fine strong{display:block;color:var(--crimson);font-weight:700}
  .contact-bar{position:absolute;left:184px;top:1100px;width:832px;height:26px;display:flex;align-items:center;justify-content:center;gap:12px;color:var(--white);font-size:13.5px;font-weight:500;white-space:nowrap}
  .contact-bar .sep{opacity:.7}
  .contact-item{display:flex;align-items:center;gap:8px}
</style>
</head>
<body>
<div class="canvas">
  <div class="flier-base"></div>
  <div class="hero-photo" role="img" aria-label="Photo of autumn trees with green, magenta and orange foliage"></div>

  <svg class="shapes" width="1200" height="1200" viewBox="0 0 1200 1200" aria-hidden="true">
    <polygon points="210,400 600,355 990,400 990,1085 210,1085" fill="var(--white)"/>
    <polygon points="223,413 600,367 977,413 977,549 223,549" fill="var(--crimson)"/>
    <rect x="223" y="562" width="242" height="523" fill="var(--panel-grey)"/>
    <rect x="733" y="562" width="244" height="523" fill="var(--panel-grey)"/>
    <polygon points="223,562 465,562 465,637 344,654 223,637" fill="var(--brick)"/>
    <polygon points="733,562 977,562 977,637 855,654 733,637" fill="var(--brick)"/>
    <rect x="465" y="562" width="268" height="523" fill="var(--peach)" style="filter:drop-shadow(0 0 6px rgba(0,0,0,.15))"/>
    <polygon points="465,562 733,562 733,653 599,670 465,653" fill="var(--crimson)"/>
  </svg>

  <div class="brand-tab">
    <span class="brand-mark"></span>
    <div class="brand-name">MAPLECREST<br>GARDENS</div>
  </div>

  <h1 class="title"><span class="title-text">2021 LANDSCAPING PACKAGES</span></h1>

  <div class="col-head" style="left:223px;width:242px;height:80px">SEASONAL CARE</div>
  <div class="col-head" style="left:465px;width:268px;height:92px;padding-left:4px">PERPETUAL CARE<br>ENDOWMENT</div>
  <div class="col-head" style="left:733px;width:244px;height:75px">BASIC CARE<br>ENDOWMENT</div>
  <div class="ribbon">MOST POPULAR</div>

  <section class="col" style="left:236px;width:222px;height:400px">
    <p class="col-sub">Seasonal Landscaping<br>grave care</p>
    <ul class="features">
      <li>Weeding and trimming services on your gravesite approximately every 7 weeks during the growing season: mid-April through mid October</li>
    </ul>
    <div class="price-block" style="top:151px"><div class="term">3 YEARS</div><div class="amount"><sup>$</sup>357</div></div>
    <div class="price-block" style="top:213px"><div class="term">2 YEARS</div><div class="amount"><sup>$</sup>238</div></div>
    <div class="price-block" style="top:275px"><div class="term">1 YEARS</div><div class="amount"><sup>$</sup>119</div></div>
    <p class="fine" style="top:343px">Multi-year payment locks in current rate<strong>VALID THROUGH 10/31/2021</strong></p>
  </section>

  <section class="col" style="left:490px;width:222px;height:400px">
    <p class="col-sub">Landscaping care forever<br>for graves with plantings</p>
    <ul class="features">
      <li style="line-height:15px">Weeding and trimming services on your gravesite approximately every 7 weeks during the growing season: mid-April through mid October</li>
      <li>Monument leveling and cleaning</li>
      <li>Payment ensures grave care forever</li>
      <li>Full bed of boxwood shrubs</li>
      <li>Replacement of shrubs</li>
      <li>Trust Certificate</li>
    </ul>
    <div class="price-block" style="top:287px"><div class="term">12 MONTHLY PAYMENTS OF</div><div class="amount"><sup>$</sup>313</div></div>
    <p class="fine" style="top:343px">Call for single payment discount<strong>VALID THROUGH 10/31/2021</strong></p>
  </section>

  <section class="col" style="left:745px;width:224px;height:400px">
    <p class="col-sub">Landscaping care forever<br>for graves with no plant-</p>
    <ul class="features">
      <li>Weeding and trimming services on your gravesite approximately every 7 weeks during the growing season: mid-April through mid October</li>
      <li style="margin-bottom:17px">Monument leveling and cleaning</li>
      <li>Payment ensures grave care forever</li>
    </ul>
    <div class="price-block" style="top:287px"><div class="term">12 MONTHLY PAYMENTS OF</div><div class="amount"><sup>$</sup>255</div></div>
    <p class="fine" style="top:343px">Call for single payment discount<strong>VALID THROUGH 10/31/2021</strong></p>
  </section>

  <footer class="contact-bar">
    <span class="contact-item">
      <svg width="15" height="15" viewBox="0 0 24 24"><path fill="#fff" d="M6.6 10.8a15.1 15.1 0 0 0 6.6 6.6l2.2-2.2a1 1 0 0 1 1-.25 11.4 11.4 0 0 0 3.6.57 1 1 0 0 1 1 1V20a1 1 0 0 1-1 1A17 17 0 0 1 3 4a1 1 0 0 1 1-1h3.5a1 1 0 0 1 1 1c0 1.25.2 2.45.57 3.57a1 1 0 0 1-.25 1z"/></svg>
      (555) 214 3380</span>
    <span class="sep">|</span>
    <span class="contact-item">
      <svg width="12" height="15" viewBox="0 0 24 30"><path fill="#fff" d="M12 0a10 10 0 0 0-10 10c0 7.5 10 20 10 20s10-12.5 10-20A10 10 0 0 0 12 0zm0 14a4 4 0 1 1 0-8 4 4 0 0 1 0 8z"/></svg>
      48 Orchard Lane, Millbrook NJ 07010</span>
    <span class="sep">|</span>
    <span class="contact-item">
      <svg width="15" height="15" viewBox="0 0 24 24" fill="none" stroke="#fff" stroke-width="2.2" stroke-linecap="round"><path d="M10 14a4 4 0 0 0 5.7 0l3.5-3.5a4 4 0 0 0-5.7-5.7L12 6.3"/><path d="M14 10a4 4 0 0 0-5.7 0l-3.5 3.5a4 4 0 0 0 5.7 5.7L12 17.7"/></svg>
      www.maplecrestgardens.org</span>
  </footer>
</div>
</body>
</html>
```